R&D and Engineering Management Consultancy Needs Branding

I need a branding style for my consultancy - specifically I need business cards by Tuesday 26 April (9 days away!) to take to a conference, including a logo design. If this service does not include printing I will need it in time for printing.

Later, the same logo and style needs to be incorporated into a Powerpoint template and a Word Template. Optionally also a Pages template.

The branding image needs to project and/or support the following qualities:
High tech
Speed and throughput
Lean
Innovation
Dependability
Quality

One possible concept is based on the Principal’s surname – Brannick, which is a small bird. So a logo design which is a stylized rendition of a bird may work well. Flight implies speed, and the style would be “techy”, perhaps geometric in a way that conveys Lean – boiling things down to the essential elements.

Other concepts are welcome.
You can find me on https://au.profilenetra.com/in/desmondbrannick

Business Card Information
Brannick Consulting
Desmond Brannick
BE (Hons), CSM, CSPO, SA
Principal Consultant
Mobile: +61 (0)455 903 617
Email: desmond@brannickconsulting.com
Web: www.brannickconsulting.com

Reverse:
Lean/Agile Software Development at Scale
Lean Product Development
Lean Portfolio Management
Organisational development and transformation
Mentoring and coaching of Technical Leaders
Program and project management
Business Processes and Systems

Target Market(s)

The target market for this consultancy comprises technology-based product and/or services development companies. They typically engage in one or a mix of software, electronics, mechanical, ASIC and MEMS development activities. They range from small startups to transnational corporations staffed by highly skilled engineers, developers and scientists. The consultancy is applicable across a range of domains such as biomedical device development, inkjet printing technology, telecommunications, internet and mesh networking technologies, renewable energy systems, and electronic product development of all kinds.

Industry/Entity Type

Information Technology

Contact Information for Business Card

Brannick Consulting
Desmond Brannick
BE (Hons), CSM, CSPO, SA
Principal Consulting

Reverse:
➢ Lean/Agile Software Development
➢ Lean Product Development
➢ Lean Portfolio Management
➢ Organisational development and transformation
➢ Mentoring and coaching of Technical Leaders
➢ Program and project management
➢ Business Processes and Systems

Logo Text

Just graphical

Font styles to use
Sans Serif

Requirements
Must have
• A clean professional look
Nice to have
• Use a bird motif based on my name Brannick
• The bird's colours are yellow/gold, light brown, black and red so these suggest a colour scheme.
• I have uploaded a stylised bird design that I like but this belongs to another company. A variation on this might be good.
Should not have
• Too much clutter. If the details are too much to fit, drop the qualifications line

```html
<!DOCTYPE html>
<html lang="en">
<head>
<meta charset="utf-8">
<title>Brannick Consulting – Business Card</title>
<link rel="stylesheet" href="https://fonts.googleapis.com/css2?family=Open+Sans:wght@400;600;700&display=swap">
<style>
  :root {
    --backdrop: #2b2b2d;
    --card: #121213;
    --card-edge: #1d1d1f;
    --gold: #f2e600;
    --ink: #f2f2f2;
    --muted: #d6d6d6;
  }
  * { box-sizing: border-box; margin: 0; padding: 0; }
  html, body {
    width: 1200px; height: 900px; overflow: hidden;
    background: var(--backdrop);
    font-family: "Open Sans", Arial, sans-serif;
  }
  .stage {
    width: 1200px; height: 900px;
    display: flex; align-items: center; justify-content: center; gap: 48px;
  }
  .card {
    width: 525px; height: 300px;
    background: var(--card);
    border: 1px solid var(--card-edge);
    border-radius: 22px;
    box-shadow: 0 18px 40px rgba(0,0,0,.45);
    position: relative;
    overflow: hidden;
  }

  /* Front */
  .card-front { display: flex; }
  .front-brand {
    width: 215px;
    display: flex; align-items: center; justify-content: center; gap: 10px;
    border-right: 1px solid rgba(255,255,255,.05);
  }
  .brand-mark {
    width: 18px; height: 18px; background: var(--gold); flex: none;
  }
  .brand-name {
    color: var(--gold); font-weight: 700; font-size: 19px; line-height: 1.15;
  }
  .front-details {
    flex: 1; padding: 78px 20px 0 26px; color: var(--ink);
  }
  .person-name { color: var(--gold); font-weight: 700; font-size: 19px; line-height: 1.2; }
  .credentials, .role { font-size: 13px; line-height: 1.5; color: var(--muted); }
  .contact-list { list-style: none; margin-top: 24px; }
  .contact-item {
    display: flex; align-items: center; gap: 12px;
    font-size: 13.5px; line-height: 1.65; color: var(--ink);
  }
  .contact-icon { width: 11px; height: 11px; flex: none; }

  /* Back */
  .card-back { padding: 46px 30px 0 40px; }
  .back-brand { display: flex; align-items: center; gap: 10px; margin-bottom: 22px; }
  .service-list { list-style: none; padding-left: 118px; }
  .service-item {
    position: relative; padding-left: 16px;
    font-size: 13px; font-weight: 600; line-height: 1.95; color: var(--ink);
  }
  .service-item::before {
    content: ""; position: absolute; left: 0; top: 10px;
    width: 6px; height: 6px; border-radius: 50%; background: var(--gold);
  }
</style>
</head>
<body>
<main class="stage">
  <section class="card card-front" aria-label="Business card front">
    <div class="front-brand">
      <span class="brand-mark"></span>
      <span class="brand-name">Brannick<br>Consulting</span>
    </div>
    <div class="front-details">
      <h1 class="person-name">Desmond Brannick</h1>
      <p class="credentials">BE (Hons), CSM, CSPO, SA</p>
      <p class="role">Principal Consulting</p>
      <ul class="contact-list">
        <li class="contact-item">
          <svg class="contact-icon" viewBox="0 0 12 12" aria-hidden="true"><path fill="#f2e600" d="M2.4 0.6l2 2.2-1 1.2c.7 1.6 2 2.9 3.6 3.6l1.2-1 2.2 2-1.2 1.8C5.2 10.2 1.8 6.8 0.6 1.8z"/></svg>
          <span>+61 (0)455 903 617</span>
        </li>
        <li class="contact-item">
          <svg class="contact-icon" viewBox="0 0 12 12" aria-hidden="true"><rect x="0.5" y="2" width="11" height="8" fill="#f2e600"/><path d="M0.5 2.5L6 6.5l5.5-4" fill="none" stroke="#121213" stroke-width="1"/></svg>
          <span>desmond@brannickconsulting.com</span>
        </li>
        <li class="contact-item">
          <svg class="contact-icon" viewBox="0 0 12 12" aria-hidden="true"><circle cx="6" cy="6" r="5.5" fill="#f2e600"/><path d="M0.8 6h10.4M6 0.5c-2.4 3-2.4 8 0 11M6 0.5c2.4 3 2.4 8 0 11" fill="none" stroke="#121213" stroke-width="0.8"/></svg>
          <span>www.brannickconsulting.com</span>
        </li>
      </ul>
    </div>
  </section>

  <section class="card card-back" aria-label="Business card back">
    <div class="back-brand">
      <span class="brand-mark"></span>
      <span class="brand-name">Brannick Consulting</span>
    </div>
    <ul class="service-list">
      <li class="service-item">Lean/Agile Software Development</li>
      <li class="service-item">Lean Product Development</li>
      <li class="service-item">Lean Portfolio Management</li>
      <li class="service-item">Organisational development and transformation</li>
      <li class="service-item">Mentoring and coaching of Technical Leaders</li>
      <li class="service-item">Program and project management</li>
      <li class="service-item">Business Processes and Systems</li>
    </ul>
  </section>
</main>
</body>
</html>
```